Name card for fertilizer industry

We 1. produce liquid fertilizer 2. gardening supply 3. Import&Export gardening related product.
I want the name card double-sided(Chinese & English version)
detail has chinese charactor for name and address.
Updates
Target Market(s)
Farmers
Industry/Entity Type
Industry
Contact Information for Business Card
Name: Daniel Lo (陳明達)
TEL: +886-48-516042
FAX:+886-48-590714
MOBILE: +886-912-804-153
ADDRESS: No.58, Baoan Rd, Dapu Township, Kexi County , TAIWAN(R.O.C) 柯溪縣大埔鎮寶安路58號
Look and feel
Each slider illustrates characteristics of the customer's brand and the style your logo design should communicate.

```html
<!DOCTYPE html>
<html lang="en">
<head>
<meta charset="utf-8">
<title>Tian He Agri Supply – Name Card</title>
<link href="https://fonts.googleapis.com/css2?family=Tinos&family=Russo+One&family=Noto+Serif+TC:wght@500;600&display=swap" rel="stylesheet">
<style>
  :root{
    --bg:#d9d9d9;
    --card:#ffffff;
    --green:#8dc63f;
    --green-deep:#3faa2e;
    --blue:#1e73c2;
    --ink-blue:#2c47a6;
    --ink-dark:#2a2a2a;
  }
  *{margin:0;padding:0;box-sizing:border-box}
  html,body{width:1200px;height:960px;overflow:hidden}
  body{background:var(--bg);position:relative;font-family:"Tinos",serif}
  .card{position:absolute;left:215px;width:770px;height:440px;background:var(--card);overflow:hidden;box-shadow:0 4px 14px rgba(0,0,0,.18)}
  .card--back{top:25px}
  .card--front{top:495px}
  .card svg.bg{position:absolute;inset:0}
  .splash{position:absolute;border-radius:50%;background:radial-gradient(closest-side,rgba(141,198,63,.9) 0%,rgba(141,198,63,.45) 45%,rgba(141,198,63,0) 100%)}
  .brand-mark{position:absolute;border-radius:50%;border:18px solid var(--green)}
  .brand-cn{position:absolute;font-family:"Noto Serif TC",serif;font-weight:600;color:var(--ink-dark);letter-spacing:2px}
  .brand-plate{position:absolute;background:var(--green);border-radius:6px;display:flex;align-items:center;justify-content:center}
  .brand-en{font-family:"Russo One",sans-serif;color:var(--ink-blue);letter-spacing:1px;white-space:nowrap}
  .person{position:absolute;left:50px;top:282px;width:360px}
  .person__name{font-size:36px;color:var(--ink-blue);letter-spacing:1px;line-height:1.1}
  .person__name-cn{font-family:"Noto Serif TC",serif;font-weight:500;font-size:24px;margin-left:14px;letter-spacing:2px}
  .person__address{margin-top:12px;font-size:14px;line-height:1.35;color:var(--ink-blue)}
  .person__address-cn{font-family:"Noto Serif TC",serif;font-weight:500;font-size:15px;margin-top:4px;color:var(--ink-blue)}
  .divider{position:absolute;left:432px;top:285px;width:1px;height:130px;background:#4d7a2a}
  .contacts{position:absolute;left:455px;top:292px;list-style:none}
  .contacts li{display:flex;align-items:center;gap:14px;height:42px;font-size:22px;color:var(--ink-blue)}
  .contacts svg{width:24px;height:24px;flex:none}
</style>
</head>
<body>

<!-- Back side -->
<section class="card card--back">
  <svg class="bg" width="770" height="440" viewBox="0 0 770 440">
    <defs>
      <linearGradient id="backBand" x1="0" y1="0" x2="0" y2="1">
        <stop offset="0" stop-color="#a6d655"/>
        <stop offset="1" stop-color="#3faa2e"/>
      </linearGradient>
    </defs>
    <path d="M0 300 Q385 265 770 250 L770 440 L0 440 Z" fill="url(#backBand)"/>
  </svg>
  <div class="splash" role="img" aria-label="Green paint splash in the top left corner" style="left:-90px;top:-90px;width:300px;height:260px"></div>
  <div class="splash" role="img" aria-label="Green paint splash in the top right corner" style="right:-100px;top:-100px;width:320px;height:280px"></div>
  <div class="brand-mark" style="left:315px;top:55px;width:140px;height:140px"></div>
  <div class="brand-cn" style="left:330px;top:200px;font-size:30px">田禾液肥</div>
  <div class="brand-plate" style="left:195px;top:245px;width:380px;height:42px">
    <span class="brand-en" style="font-size:22px">TIAN HE AGRI SUPPLY</span>
  </div>
</section>

<!-- Front side -->
<section class="card card--front">
  <svg class="bg" width="770" height="440" viewBox="0 0 770 440">
    <path d="M0 225 Q400 230 770 275 L770 440 L0 440 Z" fill="var(--blue)"/>
    <path d="M0 240 Q400 245 770 290 L770 440 L0 440 Z" fill="var(--green)"/>
    <path d="M0 240 Q400 245 770 290" fill="none" stroke="var(--green-deep)" stroke-width="3"/>
  </svg>
  <div class="splash" role="img" aria-label="Green paint splash in the top right corner" style="right:-100px;top:-100px;width:330px;height:280px"></div>
  <div class="brand-mark" style="left:50px;top:40px;width:160px;height:160px"></div>
  <div class="brand-cn" style="left:300px;top:112px;font-size:30px">田禾液肥</div>
  <div class="brand-plate" style="left:220px;top:160px;width:300px;height:36px">
    <span class="brand-en" style="font-size:18px">TIAN HE AGRI SUPPLY</span>
  </div>

  <div class="person">
    <p class="person__name">Daniel Lo<span class="person__name-cn">陳明達</span></p>
    <p class="person__address">No.58, Baoan Rd, Dapu Township, Kexi County , TAIWAN(R.O.C)</p>
    <p class="person__address-cn">柯溪縣大埔鎮寶安路58號</p>
  </div>
  <div class="divider"></div>
  <ul class="contacts">
    <li>
      <svg viewBox="0 0 24 24"><circle cx="12" cy="12" r="12" fill="var(--ink-blue)"/><path d="M6 11c0-3 12-3 12 0l-2 1-1-2H9l-1 2zM8 13h8l1 4H7z" fill="#fff"/></svg>
      +886-48-516042
    </li>
    <li>
      <svg viewBox="0 0 24 24"><circle cx="12" cy="12" r="12" fill="var(--ink-blue)"/><rect x="7" y="6" width="10" height="5" fill="#fff"/><rect x="6" y="11" width="12" height="7" rx="1" fill="#fff"/><rect x="9" y="13" width="6" height="1.5" fill="var(--ink-blue)"/></svg>
      +886-48-590714
    </li>
    <li>
      <svg viewBox="0 0 24 24"><circle cx="12" cy="12" r="12" fill="var(--ink-blue)"/><rect x="8" y="5" width="8" height="14" rx="1.5" fill="#fff"/><rect x="9.5" y="7" width="5" height="8" fill="var(--ink-blue)"/></svg>
      +886-912-804-153
    </li>
  </ul>
</section>

</body>
</html>
```